Redesign of 2 real estate websites!

We need a redesign of our two real estate websites. These websites offer detailed information on the two real estates and need a modern fresh up.
Both websites should have the same design type, so you can see that they belong together, yet they should be in different colors. There is no logo to these pages, so the headlines can be integreated into the designs.
http://www.kolbrand-villa.de
http://www.leopold-kolbrand-haus.de/

```html
<!DOCTYPE html>
<html lang="en">
<head>
<meta charset="utf-8">
<title>Die Kolbrand-Villa</title>
<link href="https://fonts.googleapis.com/css2?family=Oxygen:wght@300;400;700&family=Open+Sans:wght@400;600&display=swap" rel="stylesheet">
<style>
:root{
  --green-deep:#003d00;
  --green-mid:#0b5c12;
  --green-bright:#2a8a2a;
  --green-head:#0f5a12;
  --orange:#f0901c;
  --yellow:#fbb536;
  --text-grey:#6a6a6a;
  --text-dark:#3a3a3a;
  --rule:#d6d6d6;
  --white:#ffffff;
}
*{margin:0;padding:0;box-sizing:border-box}
html,body{width:1078px;height:1200px;overflow:hidden;background:var(--white)}
body{position:relative;font-family:"Open Sans",sans-serif;color:var(--text-grey)}
.abs{position:absolute}
.header-band{left:0;top:0;width:1078px;height:392px;
  background:radial-gradient(ellipse 560px 330px at 539px 300px,#117a1a 0%,#0a5a10 55%,var(--green-deep) 100%);}
.site-title{left:119px;top:36px;font-family:"Oxygen",sans-serif;font-weight:400;font-size:40px;color:var(--white);letter-spacing:1px}
.main-nav{left:112px;top:118px;width:854px;height:51px;display:flex;
  background:linear-gradient(#4a4a4a,#141414);}
.main-nav a{display:flex;align-items:center;padding:0 17px;color:var(--white);text-decoration:none;
  font-size:13.5px;border-right:1px solid #555;height:100%}
.main-nav a:last-child{border-right:none}
.slider{left:112px;top:168px;width:854px;height:345px;
  background:linear-gradient(180deg,#dfe6e3 0%,#b3644c 35%,#8e4e3a 60%,#4f6b33 85%,#3d4a2c 100%);}
.slider-curve{left:112px;top:500px}
.caption{left:112px;width:854px;text-align:center;color:var(--white);font-weight:600;text-shadow:0 1px 3px rgba(0,0,0,.5)}
.caption-top{top:308px;font-size:25px}
.caption-main{top:343px;font-size:32px}
.arrow{top:302px}
.dots{left:510px;top:513px;display:flex;gap:4px}
.dots span{width:11px;height:11px;border-radius:50%;background:var(--white)}
.welcome{left:112px;top:578px;width:854px;text-align:center;font-family:"Oxygen",sans-serif;font-weight:400;font-size:28px;color:var(--green-head)}
.intro{left:125px;top:621px;width:828px;text-align:center;font-size:11px;line-height:18.3px}
.divider{left:112px;top:741px;width:854px;height:1px;background:var(--rule)}
.col-title{font-family:"Oxygen",sans-serif;font-size:20px;font-weight:400}
.orange{color:var(--orange)}
.green{color:var(--green-bright)}
.photo{border:1px solid #ccc}
.sub{font-size:13px;color:#666}
.small{font-size:11px;line-height:17px;color:#888}
.btn{left:113px;top:1002px;width:90px;height:26px;border-radius:3px;
  background:linear-gradient(#2e9a30,#136a16);color:var(--white);font-size:10px;display:flex;align-items:center;justify-content:center;letter-spacing:.3px}
.post-title{font-size:13.5px;color:var(--text-dark)}
.footer{left:0;top:1088px;width:1078px;height:112px;background:linear-gradient(var(--green-mid),var(--green-deep))}
.footer-nav{left:112px;top:1113px;font-size:12px;color:var(--white)}
.footer-nav span{margin:0 6px}
.copyright{left:112px;top:1141px;font-size:11px;color:#8fb38f}
.follow{left:880px;top:1122px;display:flex;align-items:center;gap:6px;color:var(--white);font-size:12px}
.follow i{width:14px;height:14px;border-radius:50%;background:var(--white);display:block}
</style>
</head>
<body>
<div class="abs header-band"></div>
<div class="abs site-title">Die Kolbrand-Villa</div>

<nav class="abs main-nav">
  <a>HOME</a><a>MITTWEIDA</a><a>BUILDING DESIGN</a><a>OWNERS AND RESIDENTS</a><a>THE VILLA</a><a>CONTACT</a><a>RENTAL</a>
</nav>

<div class="abs slider" role="img" aria-label="Photo of the red brick villa behind trees and a garden fence"></div>
<svg class="abs slider-curve" width="854" height="45" viewBox="0 0 854 45">
  <path d="M0 8 Q427 55 854 8 L854 45 L0 45 Z" fill="#ffffff"/>
  <path d="M0 8 Q427 55 854 8 L854 14 Q427 61 0 14 Z" fill="#2a8a2a"/>
</svg>
<div class="abs caption caption-top">Proin nulla arcu nonummy luctus</div>
<div class="abs caption caption-main">Class aptent taciti sociosqu ad litora</div>
<svg class="abs arrow" style="left:104px" width="34" height="52" viewBox="0 0 34 52">
  <path d="M0 0 A26 26 0 0 1 0 52 Z" transform="translate(8 0)" fill="#fbb536"/>
  <path d="M0 0 L8 0 L8 52 L0 52 Z" fill="#fbb536"/>
  <path d="M20 16 L13 26 L20 36" fill="none" stroke="#333" stroke-width="2"/>
</svg>
<svg class="abs arrow" style="left:940px" width="34" height="52" viewBox="0 0 34 52">
  <path d="M26 0 A26 26 0 0 0 26 52 Z" fill="#fbb536"/>
  <path d="M26 0 L34 0 L34 52 L26 52 Z" fill="#fbb536"/>
  <path d="M15 16 L22 26 L15 36" fill="none" stroke="#333" stroke-width="2"/>
</svg>
<div class="abs dots"><span></span><span></span><span></span><span></span></div>

<h1 class="abs welcome">Welcome to Die Kolbrand Villa Mainpage</h1>
<p class="abs intro">Vivamus porttitor neque at volutpat rutrum purus nisi eleifend libero a tempus libero lectus feugiat felis Morbi diam mauris viverra in gravida eu mattis in ante Morbi eget arcu Morbi porta libero id ullamcorper nonummy nibh ligula pulvinar metus eget consectetuer augue nisi quis lacus Ut ac mi quis lacus mollis aliquam Curabitur iaculis tempus eros Curabitur vel mi sit amet magna malesuada ultrices Ut nisi erat fermentum vel congue id euismod in elit Fusce ultricies orci ac feugiat suscipit leo massa sodales velit et scelerisque mi tortor at ipsum Proin orci odio commodo ac gravida non</p>
<div class="abs divider"></div>

<h2 class="abs col-title orange" style="left:113px;top:774px">What’s Special</h2>
<div class="abs photo" style="left:115px;top:810px;width:239px;height:103px;background:linear-gradient(#6e8a5e,#8a8478 55%,#5d7a3e)" role="img" aria-label="Photo of a grey stone manor house"></div>
<div class="abs sub" style="left:115px;top:919px">Nunc porta convallis pede</div>
<p class="abs small" style="left:115px;top:940px;width:240px">per inceptos hymenaeos. Proin nulla arcu, nonummy luctus, dictum eget, fermentum et, lorem. Nunc porta convallis ped</p>
<div class="abs btn">LERAN MORE</div>

<h2 class="abs col-title orange" style="left:389px;top:773px">Building Designs</h2>
<div class="abs photo" style="left:389px;top:812px;width:287px;height:142px;background:linear-gradient(#9cc3e6,#e9ecef 45%,#8a6a4a)" role="img" aria-label="Photo of a white seaside villa with terrace"></div>
<div class="abs" style="left:389px;top:959px;width:93px;height:67px;background:linear-gradient(#a9c7e2,#e4e4e4 50%,#5f9a3a)" role="img" aria-label="Photo of a modern white house on a lawn"></div>
<div class="abs" style="left:487px;top:959px;width:93px;height:67px;background:linear-gradient(#27354a,#caa36a 60%,#1e2630)" role="img" aria-label="Photo of a modern house lit at dusk"></div>
<div class="abs" style="left:584px;top:959px;width:92px;height:67px;background:linear-gradient(#4c6f9c,#3a3f4a 50%,#c89a5e)" role="img" aria-label="Photo of a modern house with pool at dusk"></div>

<h2 class="abs col-title green" style="left:706px;top:774px">Recent Blog Post</h2>
<div class="abs post-title" style="left:706px;top:810px">Mauris vel lacus vitae</div>
<p class="abs small" style="left:706px;top:829px;width:260px;line-height:18.3px">Felis vestibulum volutpat. Etiam est nunc venenatis in tristique eu imperdiet ac nisl.</p>
<div class="abs post-title" style="left:706px;top:880px">Donec scelerisque leo ac risu</div>
<p class="abs small" style="left:706px;top:899px;width:260px;line-height:18.3px">orem ipsum dolor sit amet consectetuer adipiscing elit. Nam cursus. Morbi ut mi. Nullam enim leo eges-tas id condimentum at laoreet</p>
<div class="abs post-title" style="left:706px;top:971px">Curabitur vel mi sit amet</div>
<p class="abs small" style="left:706px;top:990px;width:260px;line-height:18.3px">Class aptent taciti sociosqu ad litora torquent per conubia nostra per inceptos hymenaeos</p>

<footer class="abs footer"></footer>
<div class="abs footer-nav">Home<span>|</span>Mittweida<span>|</span>Building Design<span>|</span>Owners and Residents<span>|</span>The Villa<span>|</span>Contact<span>|</span>Rental</div>
<div class="abs copyright">© 2014 Company Name.&nbsp; All right reserved.&nbsp; Term of Use</div>
<div class="abs follow"><i></i>Follow us</div>
</body>
</html>
```